3 out of 100 people will get deadly skin cancer - we need a great illustration that shows this!

We put together a prototype image that communicates lifetime skin cancer risk. (see attached). We are looking for illustrators who can take make a new/better/cooler graphic that communicates this idea. It could be as simple as a superior illustration of the graphic we have or illustrators can propose a completely different idea.What should the illustration communicate?U.S. adults have a lifetime risk of developing skin cancer of 1 in 5. But we don't want to show 1 in 5; we want to show that number in a larger group. For example, in the attached illustration we show 20 in 100 people get skin cancer (i.e., 100 beach towels/umbrellas and 20 of them are red). Research has shown that people are more likely to accurately understand numbers like this when you convey them for larger groups (i.e., 20 out of 100 rather than 1 out of 5). U.S. adults also have a lifetime risk of 2.3% of developing the deadliest form of skin cancer (melanoma). In other words, approximately 3 in 100 people will develop melanoma in their lifetime. Ideally, a single image will convey both lifetime skin cancer risk (20 in 100) and melanoma risk (3 in 100). We will award a top three as follows: 1st place = $300, 2nd place = $250, third place = $200. We will also buy any design beyond 3rd place that we like for $100. For example, we purchased 24 designs in our last contest on Artmarketly.This research is supported by funding from the Corvane Institute of Science.

Target Market(s)

The U.S. public; individuals at high risk of developing skin cancer

Industry/Entity Type

Medicine

Colors

Designer to choose colors to be used in the design.

Requirements
Must have
• an original illustration that conveys both lifetime risk of developing skin cancer (20 in 100) and melanoma (3 in 100).
Nice to have
• It can be beach towels and umbrellas, just like our prototype, or the designers can pitch an original idea. Imagery can be realistic or cartoonish (or something in between). It should be illustrations, though. Not edited photos. The image should be in color (no black and white illustrations).
Should not have
• Photos. Clip art. Free vector images.
• We are looking for original illustrations created by the designer.

```html
<!DOCTYPE html>
<html lang="en">
<head>
<meta charset="utf-8">
<title>Lifetime Skin Cancer Risk</title>
<link href="https://fonts.googleapis.com/css2?family=Arimo:wght@700&display=swap" rel="stylesheet">
<style>
  :root {
    --page: #ffffff;
    --sand-frame: #efe8b9;
    --sand: #f7f4de;
    --towel: #7fcfd2;
    --leaf: #8cc63f;
    --sun: #f6d500;
    --skin: #f2c9a8;
    --red: #b81e27;
    --red-light: #e8413a;
    --dark: #333333;
    --ink: #111111;
  }
  html, body {
    margin: 0;
    width: 1200px;
    height: 1200px;
    overflow: hidden;
    background: var(--page);
  }
  .canvas {
    position: relative;
    width: 1200px;
    height: 1200px;
    font-family: "Arimo", Arial, sans-serif;
  }
  .beach {
    position: absolute;
    left: 58px;
    top: 144px;
    width: 816px;
    height: 814px;
    box-sizing: border-box;
    background: var(--sand);
    border: 12px solid var(--sand-frame);
  }
  .crowd {
    position: absolute;
    left: 44px;
    top: 38px;
    display: grid;
    grid-template-columns: repeat(10, 66px);
    grid-auto-rows: 52px;
    column-gap: 6.6px;
    row-gap: 21px;
  }
  .spot {
    border-radius: 26px 26px 3px 3px;
    background: linear-gradient(160deg, var(--leaf) 0%, var(--sun) 50%, var(--skin) 62%, var(--towel) 72%, var(--towel) 100%);
  }
  .spot.cancer {
    background: linear-gradient(160deg, var(--red) 0%, var(--red-light) 50%, var(--red-light) 62%, var(--towel) 72%, var(--towel) 100%);
  }
  .spot.melanoma {
    background: linear-gradient(160deg, var(--red) 0%, var(--red-light) 50%, var(--red-light) 62%, var(--dark) 72%, var(--dark) 100%);
  }
  .key {
    position: absolute;
    width: 240px;
    height: 240px;
    border-radius: 50%;
    background: var(--sand-frame);
  }
  .key-inner {
    position: absolute;
    inset: 10px;
    border-radius: 50%;
    background: var(--sand);
  }
  .key-art {
    position: absolute;
    left: 22px;
    top: 14px;
    width: 176px;
    height: 116px;
    border-radius: 70px 70px 4px 4px;
  }
  .key-label {
    position: absolute;
    left: 0;
    right: 0;
    top: 142px;
    text-align: center;
    font-size: 15px;
    font-weight: 700;
    color: var(--ink);
    letter-spacing: 0.2px;
  }
  .key.no-cancer { left: 914px; top: 146px; }
  .key.skin-cancer { left: 910px; top: 432px; }
  .key.melanoma { left: 907px; top: 714px; }
  .no-cancer .key-art { background: linear-gradient(160deg, var(--leaf) 0%, var(--sun) 50%, var(--skin) 62%, var(--towel) 72%, var(--towel) 100%); }
  .skin-cancer .key-art { background: linear-gradient(160deg, var(--red) 0%, var(--red-light) 50%, var(--red-light) 62%, var(--towel) 72%, var(--towel) 100%); }
  .melanoma .key-art { background: linear-gradient(160deg, var(--red) 0%, var(--red-light) 50%, var(--red-light) 62%, var(--dark) 72%, var(--dark) 100%); }
</style>
</head>
<body>
<div class="canvas">
  <section class="beach">
    <div class="crowd">
      <div class="spot" role="img" aria-label="Sunbather under umbrella, no skin cancer"></div>
      <div class="spot cancer" role="img" aria-label="Sunbather under red umbrella, skin cancer"></div>
      <div class="spot" role="img" aria-label="Sunbather, no skin cancer"></div>
      <div class="spot" role="img" aria-label="Sunbather, no skin cancer"></div>
      <div class="spot" role="img" aria-label="Sunbather, no skin cancer"></div>
      <div class="spot" role="img" aria-label="Sunbather, no skin cancer"></div>
      <div class="spot" role="img" aria-label="Sunbather, no skin cancer"></div>
      <div class="spot" role="img" aria-label="Sunbather, no skin cancer"></div>
      <div class="spot" role="img" aria-label="Sunbather, no skin cancer"></div>
      <div class="spot" role="img" aria-label="Sunbather, no skin cancer"></div>

      <div class="spot" role="img" aria-label="Sunbather, no skin cancer"></div>
      <div class="spot" role="img" aria-label="Sunbather, no skin cancer"></div>
      <div class="spot" role="img" aria-label="Sunbather, no skin cancer"></div>
      <div class="spot cancer" role="img" aria-label="Sunbather, skin cancer"></div>
      <div class="spot" role="img" aria-label="Sunbather, no skin cancer"></div>
      <div class="spot melanoma" role="img" aria-label="Sunbather on black towel, melanoma"></div>
      <div class="spot" role="img" aria-label="Sunbather, no skin cancer"></div>
      <div class="spot" role="img" aria-label="Sunbather, no skin cancer"></div>
      <div class="spot" role="img" aria-label="Sunbather, no skin cancer"></div>
      <div class="spot cancer" role="img" aria-label="Sunbather, skin cancer"></div>

      <div class="spot" role="img" aria-label="Sunbather, no skin cancer"></div>
      <div class="spot cancer" role="img" aria-label="Sunbather, skin cancer"></div>
      <div class="spot" role="img" aria-label="Sunbather, no skin cancer"></div>
      <div class="spot" role="img" aria-label="Sunbather, no skin cancer"></div>
      <div class="spot" role="img" aria-label="Sunbather, no skin cancer"></div>
      <div class="spot" role="img" aria-label="Sunbather, no skin cancer"></div>
      <div class="spot cancer" role="img" aria-label="Sunbather, skin cancer"></div>
      <div class="spot" role="img" aria-label="Sunbather, no skin cancer"></div>
      <div class="spot" role="img" aria-label="Sunbather, no skin cancer"></div>
      <div class="spot" role="img" aria-label="Sunbather, no skin cancer"></div>

      <div class="spot" role="img" aria-label="Sunbather, no skin cancer"></div>
      <div class="spot" role="img" aria-label="Sunbather, no skin cancer"></div>
      <div class="spot melanoma" role="img" aria-label="Sunbather on black towel, melanoma"></div>
      <div class="spot cancer" role="img" aria-label="Sunbather, skin cancer"></div>
      <div class="spot" role="img" aria-label="Sunbather, no skin cancer"></div>
      <div class="spot" role="img" aria-label="Sunbather, no skin cancer"></div>
      <div class="spot" role="img" aria-label="Sunbather, no skin cancer"></div>
      <div class="spot" role="img" aria-label="Sunbather, no skin cancer"></div>
      <div class="spot" role="img" aria-label="Sunbather, no skin cancer"></div>
      <div class="spot" role="img" aria-label="Sunbather, no skin cancer"></div>

      <div class="spot" role="img" aria-label="Sunbather, no skin cancer"></div>
      <div class="spot" role="img" aria-label="Sunbather, no skin cancer"></div>
      <div class="spot" role="img" aria-label="Sunbather, no skin cancer"></div>
      <div class="spot" role="img" aria-label="Sunbather, no skin cancer"></div>
      <div class="spot" role="img" aria-label="Sunbather, no skin cancer"></div>
      <div class="spot cancer" role="img" aria-label="Sunbather, skin cancer"></div>
      <div class="spot" role="img" aria-label="Sunbather, no skin cancer"></div>
      <div class="spot cancer" role="img" aria-label="Sunbather, skin cancer"></div>
      <div class="spot" role="img" aria-label="Sunbather, no skin cancer"></div>
      <div class="spot" role="img" aria-label="Sunbather, no skin cancer"></div>

      <div class="spot cancer" role="img" aria-label="Sunbather, skin cancer"></div>
      <div class="spot" role="img" aria-label="Sunbather, no skin cancer"></div>
      <div class="spot" role="img" aria-label="Sunbather, no skin cancer"></div>
      <div class="spot" role="img" aria-label="Sunbather, no skin cancer"></div>
      <div class="spot cancer" role="img" aria-label="Sunbather, skin cancer"></div>
      <div class="spot" role="img" aria-label="Sunbather, no skin cancer"></div>
      <div class="spot" role="img" aria-label="Sunbather, no skin cancer"></div>
      <div class="spot cancer" role="img" aria-label="Sunbather, skin cancer"></div>
      <div class="spot" role="img" aria-label="Sunbather, no skin cancer"></div>
      <div class="spot" role="img" aria-label="Sunbather, no skin cancer"></div>

      <div class="spot" role="img" aria-label="Sunbather, no skin cancer"></div>
      <div class="spot" role="img" aria-label="Sunbather, no skin cancer"></div>
      <div class="spot" role="img" aria-label="Sunbather, no skin cancer"></div>
      <div class="spot cancer" role="img" aria-label="Sunbather, skin cancer"></div>
      <div class="spot" role="img" aria-label="Sunbather, no skin cancer"></div>
      <div class="spot cancer" role="img" aria-label="Sunbather, skin cancer"></div>
      <div class="spot" role="img" aria-label="Sunbather, no skin cancer"></div>
      <div class="spot" role="img" aria-label="Sunbather, no skin cancer"></div>
      <div class="spot" role="img" aria-label="Sunbather, no skin cancer"></div>
      <div class="spot" role="img" aria-label="Sunbather, no skin cancer"></div>

      <div class="spot" role="img" aria-label="Sunbather, no skin cancer"></div>
      <div class="spot" role="img" aria-label="Sunbather, no skin cancer"></div>
      <div class="spot cancer" role="img" aria-label="Sunbather, skin cancer"></div>
      <div class="spot" role="img" aria-label="Sunbather, no skin cancer"></div>
      <div class="spot cancer" role="img" aria-label="Sunbather, skin cancer"></div>
      <div class="spot" role="img" aria-label="Sunbather, no skin cancer"></div>
      <div class="spot" role="img" aria-label="Sunbather, no skin cancer"></div>
      <div class="spot" role="img" aria-label="Sunbather, no skin cancer"></div>
      <div class="spot" role="img" aria-label="Sunbather, no skin cancer"></div>
      <div class="spot cancer" role="img" aria-label="Sunbather, skin cancer"></div>

      <div class="spot" role="img" aria-label="Sunbather, no skin cancer"></div>
      <div class="spot" role="img" aria-label="Sunbather, no skin cancer"></div>
      <div class="spot" role="img" aria-label="Sunbather, no skin cancer"></div>
      <div class="spot" role="img" aria-label="Sunbather, no skin cancer"></div>
      <div class="spot" role="img" aria-label="Sunbather, no skin cancer"></div>
      <div class="spot melanoma" role="img" aria-label="Sunbather on black towel, melanoma"></div>
      <div class="spot" role="img" aria-label="Sunbather, no skin cancer"></div>
      <div class="spot" role="img" aria-label="Sunbather, no skin cancer"></div>
      <div class="spot cancer" role="img" aria-label="Sunbather, skin cancer"></div>
      <div class="spot" role="img" aria-label="Sunbather, no skin cancer"></div>

      <div class="spot" role="img" aria-label="Sunbather, no skin cancer"></div>
      <div class="spot" role="img" aria-label="Sunbather, no skin cancer"></div>
      <div class="spot" role="img" aria-label="Sunbather, no skin cancer"></div>
      <div class="spot" role="img" aria-label="Sunbather, no skin cancer"></div>
      <div class="spot" role="img" aria-label="Sunbather, no skin cancer"></div>
      <div class="spot" role="img" aria-label="Sunbather, no skin cancer"></div>
      <div class="spot" role="img" aria-label="Sunbather, no skin cancer"></div>
      <div class="spot" role="img" aria-label="Sunbather, no skin cancer"></div>
      <div class="spot" role="img" aria-label="Sunbather, no skin cancer"></div>
      <div class="spot" role="img" aria-label="Sunbather, no skin cancer"></div>
    </div>
  </section>

  <aside class="key no-cancer">
    <div class="key-inner">
      <div class="key-art" role="img" aria-label="Person lying on a blue towel under a green and yellow umbrella"></div>
      <div class="key-label">NO SKIN CANCER</div>
    </div>
  </aside>
  <aside class="key skin-cancer">
    <div class="key-inner">
      <div class="key-art" role="img" aria-label="Red-skinned person on a blue towel under a red umbrella"></div>
      <div class="key-label">SKIN CANCER</div>
    </div>
  </aside>
  <aside class="key melanoma">
    <div class="key-inner">
      <div class="key-art" role="img" aria-label="Red-skinned person on a black towel under a red umbrella"></div>
      <div class="key-label">MELANOMA</div>
    </div>
  </aside>
</div>
</body>
</html>
```